a little bit like bulkhaven but selling small amounts of high end tech gear directly to customers inbox.

Hi Designers,

I have had my artflockly logo attached to this project.
I have another web site (coolrivet.com.au)which will be dedicated mostly to
enthusiast,s that want to water cool their pc's. It's not quite finished. I may
need your help with that one once we get Gizpellbin up and running .I
like Rig Shelf Depot layout for Coolrivet
I want Giz pell to be simple to navigate, and similar to Bulkhaven.
I will be selling Enthusiast PC Components in small volumes ie first in
best dressed. weekly specials,daily specials,free shipping
There should be the ability for me to upload the component photo direct
from my Orbix5 Phone .
Links to the manufacturers website and product reviews from youtube
I will give you more in depth details tomorrow.
Updates

I would like my new site to be similar to q-Volt.com.au but cooler! Added Sunday, October 1, 2017

Target Market(s)

Enthusiast PC Builders

Industry/Entity Type

Tech

Coding

Coded - Design and coding required

Number of Pages Required

1 page

Font styles to use
Sans Serif

Colors
33b8a4

Requirements
Must have
• Link the price of my product to pricorn.com.au
• Drop down menus

```html
<!DOCTYPE html>
<html lang="en">
<head>
<meta charset="utf-8">
<title>Gizpellbin – Enthusiast PC Components</title>
<link href="https://fonts.googleapis.com/css2?family=Montserrat:wght@400;500;600;700&family=Open+Sans:wght@400;600&display=swap" rel="stylesheet">
<style>
:root{
  --teal:#33b8a4;
  --teal-dark:#2aa391;
  --ink:#333;
  --muted:#777;
  --line:#e3e3e3;
  --grey-tab:#6b6b6b;
  --nav:#4a4a4a;
  --footer:#222;
  --star:#f0a81c;
  --white:#fff;
}
*{box-sizing:border-box;margin:0;padding:0}
html,body{width:1200px;height:3025px;overflow:hidden}
body{position:relative;background:var(--white);font-family:"Open Sans",Arial,sans-serif;color:var(--ink)}
.abs{position:absolute}
ul{list-style:none}

.topbar{left:0;top:0;width:1200px;height:34px;background:var(--teal);color:var(--white);font-size:12px}
.topbar .contact{left:85px;top:9px;display:flex;gap:22px}
.topbar .account{right:85px;top:9px;display:flex;gap:18px}
.topbar span{display:flex;align-items:center;gap:6px;white-space:nowrap}
.topbar svg{width:11px;height:11px;fill:var(--white)}

.brand{left:85px;top:56px;display:flex;align-items:center;gap:8px;font-family:"Montserrat",sans-serif;font-weight:700;font-size:30px;color:#2d4c6a;letter-spacing:-.5px}
.brand .mark{width:24px;height:24px;background:var(--teal)}

.search{left:655px;top:81px;width:458px;height:36px;border:1px solid var(--line);display:flex}
.search input{flex:1;border:0;padding:0 12px;font:12px "Open Sans",sans-serif;color:#999}
.search button{width:38px;border:0;background:var(--teal);display:flex;align-items:center;justify-content:center}

.categories{left:85px;top:155px;width:270px;height:450px;border:1px solid var(--line)}
.categories h2{height:49px;background:var(--teal);color:var(--white);font:600 17px "Montserrat",sans-serif;padding:14px 20px;text-transform:uppercase}
.categories ul{padding:12px 0 0 20px}
.categories li{height:34px;display:flex;align-items:center;gap:22px;font-size:12px;color:#555}
.categories li::before{content:"";width:8px;height:8px;border:1px solid #999;border-radius:50%}

.mainnav{left:371px;top:151px;width:742px;height:53px;background:var(--nav);display:flex}
.mainnav a{flex:1;white-space:nowrap;color:var(--white);text-decoration:none;font:600 13px "Montserrat",sans-serif;text-transform:uppercase;display:flex;align-items:center;justify-content:center}
.mainnav a.active{flex:none;background:var(--teal);width:113px}

.hero{left:371px;top:204px;width:742px;height:401px;background:linear-gradient(135deg,#2e2c22 0%,#6a5a2a 35%,#3a3a30 60%,#15140f 100%)}
.hero h1{position:absolute;left:50px;top:180px;font:500 36px "Montserrat",sans-serif;color:var(--white)}
.hero p{position:absolute;left:50px;top:232px;width:380px;font-size:12px;line-height:26px;color:#eee}
.hero .dots{position:absolute;left:345px;top:374px;display:flex;gap:6px}
.hero .dots i{width:12px;height:12px;border-radius:50%;border:2px solid var(--white)}
.hero .dots i.on{background:var(--teal)}

.shelf{left:85px;width:1028px;height:420px;border:1px solid var(--line)}
.shelf .head{height:54px;border-bottom:2px solid var(--teal);position:relative}
.shelf .tab{position:absolute;left:0;top:0;height:52px;display:flex;align-items:center;gap:12px;padding:0 22px 0 12px;color:var(--white);font:600 17px "Montserrat",sans-serif;text-transform:uppercase;background:var(--grey-tab)}
.shelf .tab.teal{background:var(--teal)}
.shelf .tab .ico{width:26px;height:26px;border-radius:50%;background:var(--white);display:flex;align-items:center;justify-content:center}
.shelf .tab .ico i{width:10px;height:10px;background:var(--grey-tab);display:block}
.shelf .tab.teal .ico i{background:var(--teal)}
.shelf .arrows{position:absolute;right:12px;top:18px;color:#aaa;font-size:13px;letter-spacing:6px}
.cards{display:flex;padding-top:12px}
.card{width:257px;border-right:1px solid var(--line);height:342px;position:relative}
.card .photo{position:absolute;left:16px;top:14px;width:224px;height:240px;border-radius:2px}
.card .name{position:absolute;left:22px;top:277px;font:600 12px "Montserrat",sans-serif;color:#555;text-transform:uppercase}
.card .price{position:absolute;left:22px;top:302px;font-size:13px;display:flex;gap:6px;align-items:center;white-space:nowrap}
.price .now{color:var(--teal);font-weight:600}
.price .was{text-decoration:line-through;color:#555}
.price .stars{color:var(--star);font-size:11px;margin-left:14px;letter-spacing:-1px}
.card .tools{position:absolute;left:218px;top:128px;display:flex;flex-direction:column;gap:8px}
.card .tools span{width:24px;height:24px;border-radius:50%;border:1px solid var(--line);background:var(--white);display:flex;align-items:center;justify-content:center}
.card .tools svg{width:11px;height:11px;fill:none;stroke:#888;stroke-width:2.4}

.perks{left:0;top:2525px;width:1200px;height:162px;background:var(--teal)}
.perk{position:absolute;top:36px;display:flex;align-items:center;gap:18px;color:var(--white);font:600 18px "Montserrat",sans-serif;text-transform:uppercase;white-space:nowrap}
.perk .ring{width:88px;height:88px;border-radius:50%;border:3px solid var(--white);display:flex;align-items:center;justify-content:center}
.perk svg{width:40px;height:40px;fill:none;stroke:var(--white);stroke-width:2.5}

.footer{left:0;top:2687px;width:1200px;height:338px;background:var(--footer);color:#ddd}
.footer h3{position:absolute;top:56px;font:700 13px "Montserrat",sans-serif;color:var(--white);text-transform:uppercase;white-space:nowrap}
.footer ul{position:absolute;top:92px;font-size:11px}
.footer li{height:25.6px;display:flex;align-items:center;gap:12px;white-space:nowrap}
.footer .links li::before{content:"";border-left:5px solid #ddd;border-top:4px solid transparent;border-bottom:4px solid transparent}
.cards-pay{position:absolute;left:93px;top:90px;display:flex;gap:4px}
.cards-pay i{width:42px;height:26px;border-radius:2px;background:#d8d8d8;display:block}
.social{position:absolute;left:86px;top:150px;display:flex;gap:6px}
.social i{width:34px;height:34px;border-radius:50%;border:2px solid var(--white);display:flex;align-items:center;justify-content:center}
.social i::after{content:"";width:10px;height:10px;border-radius:50%;background:var(--white)}
.contact-list li svg{width:13px;height:13px;fill:#ddd;flex:none}
.copyright{position:absolute;left:0;width:1200px;top:292px;text-align:center;font-size:11px}
</style>
</head>
<body>

<div class="topbar abs">
  <div class="contact abs">
    <span><svg viewBox="0 0 24 24"><path d="M6.6 10.8a15 15 0 0 0 6.6 6.6l2.2-2.2c.3-.3.7-.4 1-.2 1.1.4 2.3.6 3.6.6.6 0 1 .4 1 1V20c0 .6-.4 1-1 1A17 17 0 0 1 3 4c0-.6.4-1 1-1h3.5c.6 0 1 .4 1 1 0 1.3.2 2.5.6 3.6.1.3 0 .7-.2 1z"/></svg>Call : (000)-555-0142</span>
    <span><svg viewBox="0 0 24 24"><path d="M2 5h20v14H2zm2 2v.5l8 5 8-5V7z"/></svg>Email : info@gizpellbin.com</span>
  </div>
  <div class="account abs">
    <span><svg viewBox="0 0 24 24"><path d="M12 21 3 12a5 5 0 0 1 9-6 5 5 0 0 1 9 6z"/></svg>My wishlist</span>
    <span><svg viewBox="0 0 24 24"><path d="M5 2h10l4 4v16H5z"/></svg>My Quotes</span>
    <span><svg viewBox="0 0 24 24"><circle cx="12" cy="7" r="5"/><path d="M3 22a9 9 0 0 1 18 0z"/></svg>My Account</span>
    <span><svg viewBox="0 0 24 24"><path d="M2 3h4l3 12h11l2-9H7"/><circle cx="10" cy="20" r="2"/><circle cx="18" cy="20" r="2"/></svg>Checkout</span>
    <span><svg viewBox="0 0 24 24"><path d="M3 21v-5L16 3l5 5L8 21z"/></svg>Blog</span>
  </div>
</div>

<div class="brand abs"><span class="mark"></span>gizpellbin</div>

<form class="search abs">
  <input type="text" value="Search for Products ....">
  <button type="button" aria-label="Search"><svg width="14" height="14" viewBox="0 0 24 24" fill="none" stroke="#fff" stroke-width="3"><circle cx="10" cy="10" r="7"/><path d="m15 15 6 6"/></svg></button>
</form>

<nav class="categories abs">
  <h2>Categories</h2>
  <ul>
    <li>NEW ARRIVAL</li><li>CLEARANCE</li><li>Barebone System</li><li>Build Your Own</li>
    <li>Cables/ Adaptors</li><li>CD/ DVD Drives</li><li>Computer Case/ PSU</li><li>Computer System</li>
    <li>Consumable/ FDD</li><li>Cooling/ PC Mod</li><li>CPU/ Processor</li>
  </ul>
</nav>

<nav class="mainnav abs">
  <a class="active" href="#">Home</a><a href="#">About Us</a><a href="#">Services</a><a href="#">Products</a><a href="#">News</a><a href="#">Contact Us</a>
</nav>

<section class="hero abs" role="img" aria-label="Close-up photo of a circuit board with chips">
  <h1>PC COMPONENTS</h1>
  <p>Sed ut perspiciatis unde omnis iste natus error sit voluptatem accusantium doloremque laudantium, totam rem aperiam eaque ipsa quae ab illo dicta sunt explicabo.</p>
  <div class="dots"><i></i><i class="on"></i><i></i></div>
</section>

<section class="shelf abs" style="top:664px">
  <div class="head"><div class="tab"><span class="ico"><i></i></span>Motherboard</div><div class="arrows">‹ ›</div></div>
  <div class="cards">
    <div class="card"><div class="photo" role="img" aria-label="Product photo: LCD module board" style="background:linear-gradient(135deg,#fff 15%,#4a6fa8 50%,#fff 85%)"></div>
      <div class="tools">
        <span><svg viewBox="0 0 24 24"><path d="M4 8h14l-4-4M20 16H6l4 4"/></svg></span>
        <span><svg viewBox="0 0 24 24"><path d="M12 20 4 12a4.5 4.5 0 0 1 8-5 4.5 4.5 0 0 1 8 5z"/></svg></span>
        <span><svg viewBox="0 0 24 24"><circle cx="10" cy="10" r="6"/><path d="m15 15 5 5"/></svg></span>
      </div>
      <div class="name">Product Name</div><div class="price"><span class="now">$18.60</span><span class="was">$49.90</span><span>- 63%</span><span class="stars">★★★★☆</span></div></div>
    <div class="card"><div class="photo" role="img" aria-label="Product photo: memory modules" style="background:linear-gradient(135deg,#fff 15%,#2f7a3a 50%,#fff 85%)"></div><div class="name">Product Name</div><div class="price"><span class="now">$18.60</span><span class="was">$49.90</span><span>- 63%</span><span class="stars">★★★★☆</span></div></div>
    <div class="card"><div class="photo" role="img" aria-label="Product photo: motherboard" style="background:linear-gradient(135deg,#fff 15%,#3d4a5a 50%,#fff 85%)"></div><div class="name">Product Name</div><div class="price"><span class="now">$18.60</span><span class="was">$49.90</span><span>- 63%</span><span class="stars">★★★★☆</span></div></div>
    <div class="card" style="border-right:0"><div class="photo" role="img" aria-label="Product photo: RAM stick" style="background:linear-gradient(135deg,#fff 15%,#5f9a3a 50%,#fff 85%)"></div><div class="name">Product Name</div><div class="price"><span class="now">$18.60</span><span class="was">$49.90</span><span>- 63%</span><span class="stars">★★★★☆</span></div></div>
  </div>
</section>

<section class="shelf abs" style="top:1128px">
  <div class="head"><div class="tab teal"><span class="ico"><i></i></span>PC Components</div><div class="arrows">‹ ›</div></div>
  <div class="cards">
    <div class="card"><div class="photo" role="img" aria-label="Product photo: processor chips" style="background:linear-gradient(135deg,#fff 15%,#2a2a2a 50%,#fff 85%)"></div>
      <div class="tools">
        <span><svg viewBox="0 0 24 24"><path d="M4 8h14l-4-4M20 16H6l4 4"/></svg></span>
        <span><svg viewBox="0 0 24 24"><path d="M12 20 4 12a4.5 4.5 0 0 1 8-5 4.5 4.5 0 0 1 8 5z"/></svg></span>
        <span><svg viewBox="0 0 24 24"><circle cx="10" cy="10" r="6"/><path d="m15 15 5 5"/></svg></span>
      </div>
      <div class="name">Product Name</div><div class="price"><span class="now">$18.60</span><span class="was">$49.90</span><span>- 63%</span><span class="stars">★★★★☆</span></div></div>
    <div class="card"><div class="photo" role="img" aria-label="Product photo: graphics card" style="background:linear-gradient(135deg,#fff 15%,#3a3a3a 50%,#fff 85%)"></div><div class="name">Product Name</div><div class="price"><span class="now">$18.60</span><span class="was">$49.90</span><span>- 63%</span><span class="stars">★★★★☆</span></div></div>
    <div class="card"><div class="photo" role="img" aria-label="Product photo: CPU cooler fan" style="background:linear-gradient(135deg,#fff 15%,#4a4a4a 50%,#fff 85%)"></div><div class="name">Product Name</div><div class="price"><span class="now">$18.60</span><span class="was">$49.90</span><span>- 63%</span><span class="stars">★★★★☆</span></div></div>
    <div class="card" style="border-right:0"><div class="photo" role="img" aria-label="Product photo: blue motherboard" style="background:linear-gradient(135deg,#fff 15%,#2f5fa8 50%,#fff 85%)"></div><div class="name">Product Name</div><div class="price"><span class="now">$18.60</span><span class="was">$49.90</span><span>- 63%</span><span class="stars">★★★★☆</span></div></div>
  </div>
</section>

<section class="shelf abs" style="top:1591px">
  <div class="head"><div class="tab"><span class="ico"><i></i></span>UPS/ Power</div><div class="arrows">‹ ›</div></div>
  <div class="cards">
    <div class="card"><div class="photo" role="img" aria-label="Product photo: disassembled laptop parts" style="background:linear-gradient(135deg,#fff 15%,#8a8a8a 50%,#fff 85%)"></div>
      <div class="tools">
        <span><svg viewBox="0 0 24 24"><path d="M4 8h14l-4-4M20 16H6l4 4"/></svg></span>
        <span><svg viewBox="0 0 24 24"><path d="M12 20 4 12a4.5 4.5 0 0 1 8-5 4.5 4.5 0 0 1 8 5z"/></svg></span>
        <span><svg viewBox="0 0 24 24"><circle cx="10" cy="10" r="6"/><path d="m15 15 5 5"/></svg></span>
      </div>
      <div class="name">Product Name</div><div class="price"><span class="now">$18.60</span><span class="was">$49.90</span><span>- 63%</span><span class="stars">★★★★☆</span></div></div>
    <div class="card"><div class="photo" role="img" aria-label="Product photo: power supply unit with cables" style="background:linear-gradient(135deg,#fff 15%,#2a2a2a 45%,#c9a431 65%,#fff 85%)"></div><div class="name">Product Name</div><div class="price"><span class="now">$18.60</span><span class="was">$49.90</span><span>- 63%</span><span class="stars">★★★★☆</span></div></div>
    <div class="card"><div class="photo" role="img" aria-label="Product photo: open computer case" style="background:linear-gradient(135deg,#fff 15%,#555 50%,#fff 85%)"></div><div class="name">Product Name</div><div class="price"><span class="now">$18.60</span><span class="was">$49.90</span><span>- 63%</span><span class="stars">★★★★☆</span></div></div>
    <div class="card" style="border-right:0"><div class="photo" role="img" aria-label="Product photo: assorted expansion cards" style="background:linear-gradient(135deg,#fff 15%,#4f7a3a 50%,#fff 85%)"></div><div class="name">Product Name</div><div class="price"><span class="now">$18.60</span><span class="was">$49.90</span><span>- 63%</span><span class="stars">★★★★☆</span></div></div>
  </div>
</section>

<section class="shelf abs" style="top:2055px">
  <div class="head"><div class="tab"><span class="ico"><i></i></span>Hard Disk/ Storage</div><div class="arrows">‹ ›</div></div>
  <div class="cards">
    <div class="card"><div class="photo" role="img" aria-label="Product photo: open hard disk" style="background:linear-gradient(135deg,#fff 15%,#3a3a3a 50%,#fff 85%)"></div>
      <div class="tools">
        <span><svg viewBox="0 0 24 24"><path d="M4 8h14l-4-4M20 16H6l4 4"/></svg></span>
        <span><svg viewBox="0 0 24 24"><path d="M12 20 4 12a4.5 4.5 0 0 1 8-5 4.5 4.5 0 0 1 8 5z"/></svg></span>
        <span><svg viewBox="0 0 24 24"><circle cx="10" cy="10" r="6"/><path d="m15 15 5 5"/></svg></span>
      </div>
      <div class="name">Product Name</div><div class="price"><span class="now">$18.60</span><span class="was">$49.90</span><span>- 63%</span><span class="stars">★★★★☆</span></div></div>
    <div class="card"><div class="photo" role="img" aria-label="Product photo: external drive with cable" style="background:linear-gradient(135deg,#fff 15%,#1e1e1e 50%,#fff 85%)"></div><div class="name">Product Name</div><div class="price"><span class="now">$18.60</span><span class="was">$49.90</span><span>- 63%</span><span class="stars">★★★★☆</span></div></div>
    <div class="card"><div class="photo" role="img" aria-label="Product photo: hard drive internals" style="background:linear-gradient(135deg,#fff 15%,#7a7a7a 45%,#3a6a9a 60%,#fff 85%)"></div><div class="name">Product Name</div><div class="price"><span class="now">$18.60</span><span class="was">$49.90</span><span>- 63%</span><span class="stars">★★★★☆</span></div></div>
    <div class="card" style="border-right:0"><div class="photo" role="img" aria-label="Product photo: silver hard drive" style="background:linear-gradient(135deg,#fff 15%,#9a9a9a 50%,#fff 85%)"></div><div class="name">Product Name</div><div class="price"><span class="now">$18.60</span><span class="was">$49.90</span><span>- 63%</span><span class="stars">★★★★☆</span></div></div>
  </div>
</section>

<section class="perks abs">
  <div class="perk" style="left:88px"><span class="ring"><svg viewBox="0 0 40 40"><rect x="7" y="9" width="26" height="24" rx="2"/><path d="M7 16h26M14 5v7M26 5v7"/></svg></span>Weekly Specials</div>
  <div class="perk" style="left:458px"><span class="ring"><svg viewBox="0 0 40 40"><rect x="7" y="15" width="26" height="19"/><path d="M5 10h30v5H5zM20 10v24"/></svg></span>Daily Specials</div>
  <div class="perk" style="left:818px"><span class="ring"><svg viewBox="0 0 40 40"><path d="M4 11h20v16H4zM24 16h7l5 5v6H24z"/><circle cx="11" cy="29" r="3"/><circle cx="29" cy="29" r="3"/></svg></span>Free Shipping</div>
</section>

<footer class="footer abs">
  <h3 style="left:93px">Payments Accepted</h3>
  <div class="cards-pay"><i></i><i></i><i></i><i></i></div>
  <div class="social"><i></i><i></i><i></i><i></i><i></i></div>

  <h3 style="left:361px">Information</h3>
  <ul class="links" style="left:361px"><li>About us</li><li>Customer Service</li><li>Company</li><li>Investor Relations</li><li>Advanced Search</li></ul>

  <h3 style="left:567px">Why Choose Us</h3>
  <ul class="links" style="left:567px"><li>Shopping Guide</li><li>Blog</li><li>Company</li><li>Investor Relations</li><li>Contact Us</li></ul>

  <h3 style="left:752px">My Account</h3>
  <ul class="links" style="left:752px"><li>My account</li><li>Orders</li><li>Addresses</li><li>Shopping cart</li><li>Wishlist</li></ul>

  <h3 style="left:936px">Contact Us</h3>
  <ul class="contact-list" style="left:936px">
    <li><svg viewBox="0 0 24 24"><path d="M6.6 10.8a15 15 0 0 0 6.6 6.6l2.2-2.2c.3-.3.7-.4 1-.2 1.1.4 2.3.6 3.6.6.6 0 1 .4 1 1V20c0 .6-.4 1-1 1A17 17 0 0 1 3 4c0-.6.4-1 1-1h3.5c.6 0 1 .4 1 1 0 1.3.2 2.5.6 3.6.1.3 0 .7-.2 1z"/></svg>(000)-555-0142 (Phone)</li>
    <li><svg viewBox="0 0 24 24"><path d="M6 2h12v6H6zM3 9h18v9h-3v4H6v-4H3z"/></svg>(000)-555-0142 (Fax)</li>
    <li><svg viewBox="0 0 24 24"><path d="M2 5h20v14H2zm2 2v.5l8 5 8-5V7z"/></svg><span style="text-decoration:underline">info@gizpellbin.com</span></li>
    <li style="align-items:flex-start;height:auto;padding-top:5px"><svg viewBox="0 0 24 24"><path d="M12 2a7 7 0 0 1 7 7c0 5-7 13-7 13S5 14 5 9a7 7 0 0 1 7-7zm0 4a3 3 0 1 0 0 6 3 3 0 0 0 0-6z"/></svg><span>#254 Lorem Ipsum Dummy<br>Text Lorem Ipsum</span></li>
  </ul>

  <p class="copyright">© Copyright 2017 Gizpellbin All Rights Reserved</p>
</footer>

</body>
</html>
```